SEAFOOD PACKAGING (Products for consumer)

We are looking to create packaging for various seafood products such as octopus and squid. We plan to sell our products in upscale supermarkets.

We are specializing in cut octopus this time.

Please include our company logo. Also, please leave a transparent area so that customers can see the product inside.
Updates

We want to show what is inside, so a picture of the octopus is not required. We need something simple and sophisticated.

Target Market(s)

upscale store in US and ASIA

Industry/Entity Type

Fisheries dealer

Requirements
Must have
• Please include the attached logo,Blue one is preferred.Please leave a transparent part so that the contents of the product can be seen by the consumer.1. product name on packaging →CUT OCTOPUS,TAKO SASHIMI,Highest quality,Top quality etc... 3. What text information should be on the packaging →(It may be edited, but this is the image) The raw materials are caught in a very clean environment and processed in a modern factory with ZEK certification. We are committed to additive-free products. 4. Packing size(cm/inch)→it will be about 19cm*22cm. 5. what kind of packaging do you use →PP or PA 6. dll →ai,jag
Nice to have
• https://quillmora.example/shots/4829174-Velka-Reef We need something simple and sophisticated like this one.
Should not have
• We want to show what is inside, so a picture of the octopus is not required. We need something simple and sophisticated.

```html
<!DOCTYPE html>
<html lang="en">
<head>
<meta charset="utf-8">
<title>Keldra Cut Octopus Package</title>
<link href="https://fonts.googleapis.com/css2?family=Oswald:wght@300;400;500;600;700&display=swap" rel="stylesheet">
<style>
  :root {
    --page-bg: #ffffff;
    --bag-clear: #eef0f2;
    --product-tone: #8f9599;
    --product-light: #c9cdd0;
    --navy: #0b3a75;
    --brand-blue: #0c5aa8;
    --band-dark: #0e3567;
    --label-top: #ffffff;
    --label-mid: #bcd5ea;
    --label-low: #5b97cf;
    --label-foot-top: #2a6cb6;
    --label-foot-bottom: #0552a6;
    --white: #ffffff;
  }
  html, body {
    margin: 0;
    padding: 0;
    width: 1200px;
    height: 1000px;
    overflow: hidden;
    background: var(--page-bg);
  }
  .canvas {
    position: relative;
    width: 1200px;
    height: 1000px;
    font-family: "Oswald", "Arial Narrow", sans-serif;
  }
  .package {
    position: absolute;
    left: 262px;
    top: 165px;
    width: 640px;
    height: 625px;
    background: var(--bag-clear);
  }
  .window {
    position: absolute;
    top: 60px;
    bottom: 60px;
    border-radius: 30px;
    background: linear-gradient(180deg, var(--product-light) 0%, var(--product-tone) 45%, var(--product-light) 100%);
  }
  .window--left { left: 90px; width: 115px; }
  .window--right { right: 80px; width: 100px; }
  .label {
    position: absolute;
    left: 205px;
    top: 0;
    width: 264px;
    height: 623px;
    background: linear-gradient(180deg, var(--label-top) 0%, var(--label-mid) 45%, var(--label-low) 78%, var(--label-low) 100%);
    text-align: center;
    color: var(--navy);
  }
  .brand {
    position: absolute;
    top: 160px;
    left: 0;
    right: 0;
    display: flex;
    align-items: center;
    justify-content: center;
    gap: 12px;
  }
  .brand__mark {
    width: 22px;
    height: 22px;
    border-radius: 50%;
    background: var(--brand-blue);
  }
  .brand__name {
    font-weight: 700;
    font-size: 56px;
    letter-spacing: 5px;
    line-height: 1;
    color: var(--brand-blue);
  }
  .product {
    position: absolute;
    top: 322px;
    left: 0;
    right: 0;
  }
  .product__grade {
    font-weight: 400;
    font-size: 22px;
    line-height: 1;
    margin-bottom: 8px;
  }
  .product__name {
    font-weight: 600;
    font-size: 37px;
    line-height: 1.02;
    letter-spacing: -0.3px;
  }
  .claim {
    position: absolute;
    top: 489px;
    left: 0;
    right: 0;
    height: 46px;
    background: var(--band-dark);
    color: var(--white);
    font-weight: 300;
    font-size: 7px;
    line-height: 1.35;
    display: flex;
    align-items: center;
    justify-content: center;
  }
  .footer {
    position: absolute;
    top: 535px;
    left: 0;
    right: 0;
    bottom: 0;
    background: linear-gradient(180deg, var(--label-foot-top), var(--label-foot-bottom));
    color: var(--white);
  }
  .footer__weight {
    margin-top: 20px;
    font-weight: 400;
    font-size: 17px;
    line-height: 1;
  }
  .footer__care {
    margin-top: 5px;
    font-weight: 400;
    font-size: 8px;
    letter-spacing: 0.2px;
  }
</style>
</head>
<body>
<div class="canvas">
  <div class="package">
    <div class="window window--left" role="img" aria-label="Clear window showing frozen cut octopus pieces inside the bag"></div>
    <div class="window window--right" role="img" aria-label="Clear window showing frozen cut octopus pieces inside the bag"></div>

    <div class="label">
      <div class="brand">
        <span class="brand__mark"></span>
        <span class="brand__name">KELDRA</span>
      </div>

      <div class="product">
        <div class="product__grade">TOP QUALITY</div>
        <div class="product__name">Cut Octopus<br>Tako Sashimi</div>
      </div>

      <div class="claim">
        <p style="margin:0">The raw materials are caught in a very clean environment<br>and processed in a modern factory with ZEK certification.<br>We are committed to additive-free products.</p>
      </div>

      <div class="footer">
        <div class="footer__weight">NET WT. 32 OZ (2.0LB) 907g</div>
        <div class="footer__care">KEEP FROZEN • THAW BEFORE COOKING</div>
      </div>
    </div>
  </div>
</div>
</body>
</html>
```